Stationary and Business Card
Medical Practice
I need single sided standard sized Business Card [3.5" x 2"]
Letter type / font / color is up to the designer.
Professional
Benedict Harwell, MD
Torrance Ridge-Velmont Building
Suite 460
4127 Almaden Avenue
La Jolla, CA 92037
contact@brinmoor-example.com
www.drharwell-example.com
Please use provided logo.
Please visit drharwell-example.com for any additional creative direction.
Do not include email address.
Please provide a version with www.drharwell-example.com on the back of the card and a version with the web address on the front.

```html
<!DOCTYPE html>
<html lang="en">
<head>
<meta charset="utf-8">
<title>Harwell Facial Plastic Surgery — Business Cards</title>
<link rel="stylesheet" href="https://fonts.googleapis.com/css2?family=Open+Sans:wght@400;700&family=PT+Serif:wght@400&display=swap">
<style>
  :root {
    --page: #e9e6e2;
    --card: #ffffff;
    --navy: #2b1f7d;
    --blue: #1e63c4;
    --sky: #1f9be0;
    --brown: #5a3a22;
    --ink: #555a60;
    --rule: #c9c9c9;
  }
  html, body {
    margin: 0;
    width: 1200px;
    height: 852px;
    overflow: hidden;
    background: var(--page);
  }
  .canvas { position: relative; width: 1200px; height: 852px; }
  .card {
    position: absolute;
    width: 560px;
    height: 320px;
    background: var(--card);
    border-radius: 18px;
    overflow: hidden;
    box-shadow: 0 6px 18px rgba(0,0,0,.18);
  }
  .card--side { left: 40px; top: 140px; }
  .card--stacked { left: 600px; top: 400px; }
  .card .edges { position: absolute; inset: 0; width: 100%; height: 100%; }

  .wordmark {
    position: absolute;
    display: flex;
    align-items: center;
    gap: 12px;
    font-family: "Open Sans", Arial, sans-serif;
    font-weight: 700;
    color: var(--navy);
    line-height: 1;
  }
  .wordmark .mark-square { background: var(--blue); display: block; flex: none; }

  .name {
    position: absolute;
    font-family: "Open Sans", Arial, sans-serif;
    font-weight: 700;
    color: var(--blue);
    margin: 0;
    white-space: nowrap;
  }
  .address {
    position: absolute;
    font-family: "PT Serif", Georgia, serif;
    color: var(--ink);
    margin: 0;
    line-height: 1.4;
    white-space: nowrap;
  }
  .contacts {
    position: absolute;
    list-style: none;
    margin: 0;
    padding: 0;
    font-family: "Open Sans", Arial, sans-serif;
    color: var(--ink);
    white-space: nowrap;
  }
  .contacts li { display: flex; align-items: center; gap: 8px; line-height: 1.75; }
  .contacts svg { width: 11px; height: 11px; fill: var(--blue); flex: none; }
  .divider { position: absolute; width: 1px; background: var(--rule); }

  /* card with logo left */
  .card--side .wordmark { left: 36px; top: 144px; font-size: 28px; }
  .card--side .mark-square { width: 24px; height: 24px; }
  .card--side .divider { left: 258px; top: 62px; height: 200px; }
  .card--side .name { left: 272px; top: 40px; font-size: 19px; }
  .card--side .address { left: 272px; top: 92px; font-size: 13.5px; }
  .card--side .contacts { left: 272px; top: 178px; font-size: 13px; }

  /* card with logo on top */
  .card--stacked .wordmark { left: 50px; top: 68px; font-size: 40px; }
  .card--stacked .mark-square { width: 36px; height: 36px; }
  .card--stacked .name { left: 50px; top: 168px; font-size: 17px; }
  .card--stacked .address { left: 50px; top: 200px; font-size: 13px; }
  .card--stacked .divider { left: 264px; top: 168px; height: 100px; }
  .card--stacked .contacts { left: 278px; top: 166px; font-size: 12.5px; }
</style>
</head>
<body>
<main class="canvas">

  <section class="card card--side" aria-label="Business card, logo beside details">
    <svg class="edges" viewBox="0 0 560 320" aria-hidden="true">
      <defs>
        <linearGradient id="band-a" x1="0" y1="0" x2="0" y2="1">
          <stop offset="0" stop-color="#2b1f7d"/>
          <stop offset=".55" stop-color="#1e63c4"/>
          <stop offset="1" stop-color="#2b1f7d"/>
        </linearGradient>
      </defs>
      <path d="M560 0 H512 C548 90 548 220 488 320 H560 Z" fill="url(#band-a)"/>
      <path d="M498 0 C536 95 534 225 474 320" fill="none" stroke="#5a3a22" stroke-width="4"/>
      <path d="M0 250 C40 290 90 310 150 320 H0 Z" fill="url(#band-a)"/>
      <path d="M0 232 C50 285 110 312 175 320" fill="none" stroke="#5a3a22" stroke-width="3"/>
    </svg>
    <div class="wordmark"><span class="mark-square"></span>Harwell</div>
    <div class="divider"></div>
    <h2 class="name">Benedict Harwell, MD</h2>
    <p class="address">Torrance Ridge-Velmont Building<br>Suite 460, 4127 Almaden Avenue<br>La Jolla, CA 92037</p>
    <ul class="contacts">
      <li><svg viewBox="0 0 12 12"><path d="M2.5 0.5 L4.5 2.8 L3.4 4.2 C4.2 5.9 6 7.7 7.8 8.6 L9.2 7.5 L11.5 9.5 L10 11.5 C5 11 1 7 0.5 2 Z"/></svg>858.555.0147</li>
      <li><svg viewBox="0 0 12 12"><path d="M2 4 H10 V11 H2 Z M3 0.5 H9 V3.5 H3 Z"/></svg>858-555-0192</li>
      <li><svg viewBox="0 0 12 12"><circle cx="6" cy="6" r="5.5"/></svg>www.drharwell-example.com</li>
    </ul>
  </section>

  <section class="card card--stacked" aria-label="Business card, logo above details">
    <svg class="edges" viewBox="0 0 560 320" aria-hidden="true">
      <defs>
        <linearGradient id="band-b" x1="0" y1="0" x2="0" y2="1">
          <stop offset="0" stop-color="#2b1f7d"/>
          <stop offset=".55" stop-color="#1f9be0"/>
          <stop offset="1" stop-color="#2b1f7d"/>
        </linearGradient>
      </defs>
      <path d="M560 0 H512 C548 90 548 220 488 320 H560 Z" fill="url(#band-b)"/>
      <path d="M498 0 C536 95 534 225 474 320" fill="none" stroke="#5a3a22" stroke-width="4"/>
      <path d="M0 0 H70 C40 20 15 45 0 70 Z" fill="url(#band-b)"/>
      <path d="M0 262 C45 298 95 314 160 320 H0 Z" fill="url(#band-b)"/>
      <path d="M0 244 C55 292 115 314 185 320" fill="none" stroke="#5a3a22" stroke-width="3"/>
    </svg>
    <div class="wordmark"><span class="mark-square"></span>Harwell</div>
    <h2 class="name">Benedict Harwell, MD</h2>
    <p class="address">Torrance Ridge-Velmont Building<br>Suite 460, 4127 Almaden Avenue<br>La Jolla, CA 92037</p>
    <div class="divider"></div>
    <ul class="contacts">
      <li><svg viewBox="0 0 12 12"><path d="M2.5 0.5 L4.5 2.8 L3.4 4.2 C4.2 5.9 6 7.7 7.8 8.6 L9.2 7.5 L11.5 9.5 L10 11.5 C5 11 1 7 0.5 2 Z"/></svg>858.555.0147</li>
      <li><svg viewBox="0 0 12 12"><path d="M2 4 H10 V11 H2 Z M3 0.5 H9 V3.5 H3 Z"/></svg>858-555-0192</li>
      <li><svg viewBox="0 0 12 12"><circle cx="6" cy="6" r="5.5"/></svg>www.drharwell-example.com</li>
    </ul>
  </section>

</main>
</body>
</html>
```